The Harvest Compass

Cutting Through the Noise to What Actually Works.

Nutrition book

Target Market(s)

People looking to be or get healthy and eat right.

```html
<!DOCTYPE html>
<html lang="en">
<head>
<meta charset="utf-8">
<title>The Harvest Compass — Book Cover</title>
<link rel="stylesheet" href="https://fonts.googleapis.com/css2?family=Oswald:wght@500;600;700&display=swap">
<style>
  :root {
    --page-bg: #ffffff;
    --cover-yellow: #f3b51f;
    --cover-yellow-light: #f6c22c;
    --title-white: #ffffff;
    --title-red: #c3221d;
    --title-black: #121212;
    --subtitle-navy: #17354d;
    --scene-red: #c42a22;
    --scene-light: #e9e6e2;
  }
  html, body {
    margin: 0;
    padding: 0;
    width: 1200px;
    height: 1200px;
    overflow: hidden;
    background: var(--page-bg);
  }
  .book-cover {
    position: absolute;
    left: 220px;
    top: 20px;
    width: 760px;
    height: 1160px;
    background: linear-gradient(160deg, var(--cover-yellow-light) 0%, var(--cover-yellow) 60%, #efaa1a 100%);
    font-family: "Oswald", "Arial Narrow", sans-serif;
    text-align: center;
    text-transform: uppercase;
  }
  .title { margin: 0; font-weight: 700; }
  .title-line {
    position: absolute;
    left: 0;
    right: 0;
    line-height: 1;
    white-space: nowrap;
  }
  .title-the {
    top: 119px;
    color: var(--title-white);
    font-size: 80px;
    letter-spacing: 2px;
  }
  .title-harvest {
    top: 206px;
    color: var(--title-red);
    font-size: 148px;
    letter-spacing: 10px;
    padding-left: 10px;
  }
  .title-compass {
    top: 356px;
    color: var(--title-black);
    font-size: 135px;
    letter-spacing: 7px;
    padding-left: 7px;
  }
  .subtitle {
    position: absolute;
    left: 0;
    right: 0;
    top: 525px;
    margin: 0;
    color: var(--subtitle-navy);
    font-weight: 600;
    font-size: 56px;
    line-height: 1.16;
    letter-spacing: 0.5px;
  }
  .subtitle .full-stop { color: var(--title-red); }
  .place-setting {
    position: absolute;
    left: 170px;
    top: 685px;
    width: 450px;
    height: 335px;
    background: linear-gradient(180deg, var(--scene-red) 0%, var(--scene-light) 45%, var(--scene-light) 60%, var(--scene-red) 100%);
    opacity: 0.85;
  }
</style>
</head>
<body>
  <main class="book-cover">
    <h1 class="title">
      <span class="title-line title-the">The</span>
      <span class="title-line title-harvest">Harvest</span>
      <span class="title-line title-compass">Compass</span>
    </h1>
    <p class="subtitle">Cutting through the noise<br>to what actually works<span class="full-stop">.</span></p>
    <div class="place-setting" role="img" aria-label="Photograph of a white pillow resting on a red dinner plate, with a fork on the left and a knife on the right"></div>
  </main>
</body>
</html>
```